Experienced Home remodel service

I'm a home remodeler. I want a catch phrase that clearly describes viewers what kind of work I'm in like the purple phrase on my rough draft idea. I need my website, phone, logo, slogan included. The picture is of my daughter. I want her on it. Be cool if something could be added to her picture like a hard hat or tool belt ect and her picture cut out/background removed. Some kind of background other than plain white for whole picture. I added extra pics of her so pick one

Target Market(s)

Home owners between 30-60

Industry/Entity Type

Home renovation/remodel

Colors

Designer to choose colors to be used in the design.

Requirements
Must have
• Daughters picture incorporated. Logo, phone, website address, slogan,
Nice to have
• See a hardhat or tool belt added to one of my daughters pictures that is chosen to use by designer

```html
<!DOCTYPE html>
<html lang="en">
<head>
<meta charset="utf-8">
<title>Harlow Home Works – Billboard</title>
<link href="https://fonts.googleapis.com/css2?family=Montserrat:wght@500;700;800&family=Saira+Semi+Condensed:wght@800&display=swap" rel="stylesheet">
<style>
  :root {
    --page: #eef0f2;
    --ink: #111111;
    --paper: #ffffff;
    --silver-dark: #a9a9a9;
    --muted: #8a8a8a;
    --photo-top: #e9dcf0;
    --photo-mid: #cdb7de;
    --photo-accent: #e8c64a;
  }
  * { margin: 0; padding: 0; box-sizing: border-box; }
  html, body {
    width: 1200px; height: 834px; overflow: hidden;
    background: var(--page);
  }
  .billboard {
    position: absolute; left: 20px; top: 117px;
    width: 1160px; height: 600px;
    background: var(--paper);
    overflow: hidden;
    box-shadow: 0 6px 24px rgba(0,0,0,.18);
  }
  .billboard__shapes { position: absolute; inset: 0; }
  .brand {
    position: absolute; left: 24px; top: 200px; width: 340px;
    text-align: center;
  }
  .brand__mark {
    width: 22px; height: 22px; background: var(--ink);
    margin: 0 auto 16px;
  }
  .brand__name {
    font-family: "Montserrat", sans-serif; font-weight: 800;
    font-size: 29px; line-height: 1.08; letter-spacing: 2px;
    color: var(--ink); text-transform: uppercase;
  }
  .brand__slogan {
    margin-top: 18px;
    font-family: "Montserrat", sans-serif; font-weight: 500;
    font-size: 16px; letter-spacing: 1.5px; color: var(--muted);
    white-space: nowrap;
  }
  .hero-photo {
    position: absolute; left: 385px; top: 24px;
    width: 270px; height: 420px;
    border-radius: 130px 130px 8px 8px;
    background: linear-gradient(180deg, var(--photo-accent) 0 12%, var(--photo-top) 12% 40%, var(--photo-mid) 100%);
  }
  .headline {
    position: absolute; left: 665px; top: 40px; width: 470px;
    font-family: "Saira Semi Condensed", "Arial Narrow", sans-serif; font-weight: 800;
    font-size: 72px; line-height: 1; text-align: center;
    color: var(--paper); text-transform: uppercase;
    white-space: nowrap;
  }
  .contact {
    position: absolute; left: 40px; right: 40px; top: 488px;
    display: flex; align-items: center; gap: 44px;
    font-family: "Montserrat", sans-serif; font-weight: 700; color: var(--ink);
    white-space: nowrap;
  }
  .contact__item { display: flex; align-items: center; gap: 12px; }
  .contact__phone { font-size: 56px; letter-spacing: -1px; }
  .contact__web { font-size: 38px; letter-spacing: -.5px; }
  .contact__icon { flex: none; }
</style>
</head>
<body>
  <section class="billboard">
    <svg class="billboard__shapes" viewBox="0 0 1160 600" width="1160" height="600" aria-hidden="true">
      <defs>
        <linearGradient id="band" x1="0" y1="0" x2="0" y2="1">
          <stop offset="0" stop-color="#e6e6e6"/>
          <stop offset="1" stop-color="#c9c9c9"/>
        </linearGradient>
      </defs>
      <path d="M500 0 H1160 V330 C1010 395 840 445 600 470 H500 Z" fill="var(--ink)"/>
      <path d="M0 418 C220 392 420 430 610 462 C840 452 1000 402 1160 318 V600 H0 Z" fill="var(--silver-dark)"/>
      <path d="M0 432 C220 408 420 446 610 478 C840 468 1000 418 1160 336 V600 H0 Z" fill="var(--paper)"/>
      <path d="M0 446 C220 424 420 462 610 492 C840 484 1000 436 1160 354 V600 H0 Z" fill="url(#band)"/>
    </svg>

    <div class="brand">
      <div class="brand__mark"></div>
      <div class="brand__name">Harlow Home<br>Works</div>
      <div class="brand__slogan">BUILD - REPAIR - REPLACE</div>
    </div>

    <div class="hero-photo" role="img" aria-label="Cut-out photo of a smiling young girl in a yellow hard hat and lilac puffer jacket, holding a hammer"></div>

    <h1 class="headline">For all<br>your home<br>remodel<br>needs</h1>

    <div class="contact">
      <div class="contact__item contact__phone">
        <svg class="contact__icon" width="44" height="44" viewBox="0 0 44 44" aria-hidden="true">
          <circle cx="22" cy="22" r="20" fill="var(--ink)"/>
          <path d="M15 12c1.5-1 3-.6 3.8.8l2 3.4c.6 1.1.3 2.2-.6 3l-1.3 1.1c1 2.3 2.8 4.1 5 5l1.1-1.3c.8-.9 1.9-1.2 3-.6l3.4 2c1.4.8 1.8 2.3.8 3.8-1.3 1.9-3.4 2.8-5.6 2.1C20.3 30.6 13.4 23.7 12.9 17.6c-.2-2.2.6-4.300 2.1-5.6z" fill="var(--paper)"/>
        </svg>
        <span>555-014-2273</span>
      </div>
      <div class="contact__item contact__web">
        <svg class="contact__icon" width="36" height="36" viewBox="0 0 36 36" aria-hidden="true" fill="none" stroke="var(--ink)" stroke-width="2.6">
          <circle cx="18" cy="18" r="15"/>
          <ellipse cx="18" cy="18" rx="6.5" ry="15"/>
          <path d="M3 18h30M5.5 10h25M5.5 26h25"/>
        </svg>
        <span>harlowhomeworks.com</span>
      </div>
    </div>
  </section>
</body>
</html>
```